Startup in search for creative and funky label for a food product

We, Vindmark Food Lab need a label for a new product: extra virgin oil from roasted sunflower seeds. The oil is produced at family gardens in sunny Kakheti region in Western Georgia.
Our goal is to introduce this new exclusive product, unknown in Western Europe. The test panels in Sweden liked the product and we hope to sell both for foodies and general public.
The feeling of the label shoud be both creative and exclusive. Maybe even funky, please see the file attached.

We would like to have the label in English and Swedish. Maybe we can do it in English first, since not all of you would understand Swedish, the Swedish design would be identical. The document below has both English and Swedish text.

We attachthe image of the bottle, please do not consider the label on the bottle, it is just an example.

Target Market(s)

General Market in Sweden and Europe. First priority: foddies, restaurants, specialized food stores.

Industry/Entity Type

Online Shopping

Requirements
Must have
• We would need the design in two languages, the same design for Swedish and English, but two separated labels. Once we agree on the English version, we can do the same for Swedish.
Nice to have
• Feeling of locally grown sunflowers, eye-catching.
Should not have
• Classic design for oil

```html
<!DOCTYPE html>
<html lang="en">
<head>
<meta charset="utf-8">
<title>Extra Virgin Oil – Roasted Sunflower Seeds Label</title>
<link rel="stylesheet" href="https://fonts.googleapis.com/css2?family=Cinzel+Decorative:wght@700&family=Oswald:wght@400;500&family=Fjalla+One&display=swap">
<style>
  :root {
    --page: #f1f1f0;
    --sky-light: #2aa3d6;
    --sky-deep: #0b6aa6;
    --sun: #f2b324;
    --sun-soft: #f7d35a;
    --leaf: #3f9a45;
    --ink: #0c1d33;
    --white: #ffffff;
  }
  html, body {
    margin: 0;
    width: 1200px;
    height: 872px;
    overflow: hidden;
    background: var(--page);
  }
  .label {
    position: absolute;
    left: 347px;
    top: 36px;
    width: 505px;
    height: 800px;
    display: block;
  }
  .label__ground { fill: url(#skyWash); }
  .premium {
    font-family: "Cinzel Decorative", serif;
    font-weight: 700;
    font-size: 40px;
    letter-spacing: 3px;
    fill: var(--white);
    stroke: var(--ink);
    stroke-width: 1.2px;
    paint-order: stroke;
  }
  .title {
    font-family: "Oswald", sans-serif;
    font-weight: 500;
    font-size: 80px;
    letter-spacing: 2px;
    fill: var(--sun);
  }
  .origin {
    font-family: "Fjalla One", sans-serif;
    font-size: 27px;
    fill: var(--ink);
  }
  .origin--small { font-size: 19px; }
  .claim {
    font-family: "Fjalla One", sans-serif;
    font-size: 20px;
    letter-spacing: 1px;
    fill: var(--ink);
  }
  .maker-mark { fill: var(--ink); }
  .maker-name {
    font-family: "Fjalla One", sans-serif;
    font-size: 12px;
    letter-spacing: 0.5px;
    fill: var(--sun);
  }
  .volume {
    font-family: "Fjalla One", sans-serif;
    font-size: 26px;
    fill: var(--ink);
  }
</style>
</head>
<body>
<svg class="label" viewBox="0 0 505 800" xmlns="http://www.w3.org/2000/svg" aria-label="Sunflower oil label">
  <defs>
    <linearGradient id="skyWash" x1="0" y1="0" x2="1" y2="1">
      <stop offset="0" stop-color="var(--sky-light)"/>
      <stop offset="1" stop-color="var(--sky-deep)"/>
    </linearGradient>
    <radialGradient id="bloomFill" cx="0.5" cy="0.5" r="0.5">
      <stop offset="0.3" stop-color="var(--sun-soft)"/>
      <stop offset="1" stop-color="var(--sun)"/>
    </radialGradient>
    <linearGradient id="fieldFill" x1="0" y1="0" x2="0" y2="1">
      <stop offset="0" stop-color="var(--sun)"/>
      <stop offset="0.6" stop-color="var(--sun-soft)"/>
      <stop offset="1" stop-color="var(--leaf)"/>
    </linearGradient>
    <path id="premiumArc" d="M 90 120 Q 252 40 415 120"/>
    <path id="leftArc" d="M 110 700 Q 150 620 225 610"/>
    <path id="rightArc" d="M 280 610 Q 360 620 400 700"/>
  </defs>

  <rect class="label__ground" x="0" y="0" width="505" height="800"/>

  <text class="premium" text-anchor="middle"><textPath href="#premiumArc" startOffset="50%">PREMIUM</textPath></text>

  <text class="title" x="252" y="190" text-anchor="middle">EXTRA</text>
  <text class="title" x="252" y="272" text-anchor="middle">VIRGIN</text>

  <circle class="title-bloom" cx="212" cy="350" r="56" fill="url(#bloomFill)" role="img" aria-label="Sunflower blossom illustration forming the letter O"/>
  <text class="title" x="274" y="364">IL</text>

  <text class="origin" x="252" y="466" text-anchor="middle">FROM ROASTED</text>
  <text class="origin" x="252" y="498" text-anchor="middle">SUNFLOWER SEEDS</text>
  <text class="origin origin--small" x="252" y="532" text-anchor="middle">FROM FAMILY GARDENS</text>
  <text class="origin origin--small" x="252" y="554" text-anchor="middle">IN KAKHETI</text>

  <rect class="sunflower-field" x="0" y="570" width="505" height="230" fill="url(#fieldFill)" role="img" aria-label="Illustration of sunflower heads with green leaves"/>

  <text class="claim"><textPath href="#leftArc">UNREFINED</textPath></text>
  <text class="claim"><textPath href="#rightArc">ALL NATURAL</textPath></text>

  <circle class="maker-mark" cx="252" cy="652" r="46"/>
  <text class="maker-name" x="252" y="650" text-anchor="middle">VINDMARK</text>
  <text class="maker-name" x="252" y="666" text-anchor="middle">FOOD LAB</text>

  <text class="volume" x="252" y="762" text-anchor="middle">250 ML</text>
</svg>
</body>
</html>
```